Revise / change slightly the wrap, box and label design. Minor changes only.

We're looking to make some slight changes in positioning and text / colours on our previous packaging. All descriptions will be detailed.

```html
<!DOCTYPE html>
<html lang="en">
<head>
<meta charset="utf-8">
<title>Sea Pines — Shimmer Window Cleaner label options</title>
<link rel="stylesheet" href="https://fonts.googleapis.com/css2?family=Bebas+Neue&family=Nunito:wght@300;400;700;800&family=Merriweather:ital,wght@1,300;1,400&display=swap">
<style>
  :root {
    --page: #ffffff;
    --kraft: #d8b989;
    --kraft-deep: #cfae7c;
    --sky: #b4cae8;
    --ink: #0a0a0a;
    --slate-blue: #7c98c8;
    --stamp-blue: #6f8fc4;
    --white: #ffffff;
  }
  * { box-sizing: border-box; margin: 0; padding: 0; }
  html, body { width: 1200px; height: 597px; overflow: hidden; background: var(--page); }
  .sheet { position: relative; width: 1200px; height: 597px; }

  .label {
    position: absolute; top: 71px; width: 324px; height: 453px;
    background: var(--sky); overflow: hidden;
  }
  .label--one { left: 66px; }
  .label--two { left: 438px; }
  .label--three { left: 810px; }

  .label__kraft {
    position: absolute; left: 0; top: 0; width: 100%; height: 235px;
    background: radial-gradient(ellipse at 40% 40%, var(--kraft) 0%, var(--kraft-deep) 100%);
  }

  .brand {
    position: absolute; left: 91px; top: 40px;
    display: flex; align-items: center; gap: 8px;
    font-family: "Nunito", sans-serif; font-weight: 800;
    font-size: 34px; line-height: 1; color: var(--ink); letter-spacing: -0.5px;
  }
  .brand__dot { width: 12px; height: 12px; border-radius: 50%; background: var(--ink); }

  .seal { position: absolute; left: 175px; top: 96px; width: 88px; height: 88px; }

  .variant {
    position: absolute; left: 73px; top: 186px;
    font-size: 18px; line-height: 1; white-space: nowrap;
  }
  .variant--serif { font-family: "Merriweather", serif; font-style: italic; font-weight: 300; color: var(--slate-blue); }
  .variant--bold-dark { font-family: "Nunito", sans-serif; font-weight: 800; color: var(--ink); left: 74px; }
  .variant--bold-blue { font-family: "Nunito", sans-serif; font-weight: 800; color: var(--slate-blue); left: 74px; }

  .product {
    position: absolute; left: 67px; top: 206px;
    font-family: "Bebas Neue", sans-serif; font-size: 64px; line-height: 1;
    color: var(--ink); letter-spacing: 0.5px;
    -webkit-text-stroke: 1px var(--ink);
  }

  .tagline {
    position: absolute; left: 70px; top: 313px;
    font-family: "Merriweather", serif; font-style: italic; font-weight: 300;
    font-size: 19px; color: var(--slate-blue); white-space: nowrap;
  }

  .warning {
    position: absolute; left: 294px; top: 431px;
    transform: rotate(-90deg); transform-origin: 0 0;
    font-family: "Nunito", sans-serif; font-weight: 300;
    font-size: 14.5px; line-height: 1; white-space: nowrap;
  }
  .warning--blue { color: var(--slate-blue); }
  .warning--white { color: var(--white); }

  .volume-box {
    position: absolute; left: 216px; top: 379px; width: 48px; height: 53px;
    border: 1px solid var(--slate-blue);
    font-family: "Nunito", sans-serif; text-align: center;
  }
  .volume-box__origin { height: 35px; padding-top: 3px; font-size: 9px; line-height: 1; color: var(--slate-blue); }
  .volume-box__wave { display: block; margin: 2px auto 2px; }
  .volume-box__size {
    height: 17px; border-top: 1px solid var(--slate-blue);
    font-size: 12.5px; line-height: 16px; color: var(--ink);
  }
</style>
</head>
<body>
<main class="sheet">

  <section class="label label--one">
    <div class="label__kraft"></div>
    <div class="brand"><span>Sea Pines</span><span class="brand__dot"></span></div>
    <svg class="seal" viewBox="0 0 88 88" role="img" aria-label="Recycled bottle badge">
      <circle cx="44" cy="44" r="42" fill="none" stroke="var(--stamp-blue)" stroke-width="2"/>
      <circle cx="44" cy="44" r="26" fill="none" stroke="var(--stamp-blue)" stroke-width="1.5"/>
    </svg>
    <p class="variant variant--serif">Window Cleaner</p>
    <h1 class="product">SHIMMER</h1>
    <p class="tagline">Drop In, Clean Up</p>
    <div class="volume-box">
      <div class="volume-box__origin">Seacliff
        <svg class="volume-box__wave" width="30" height="4" viewBox="0 0 30 4"><path d="M1 3 Q15 0 29 2" fill="none" stroke="var(--slate-blue)" stroke-width="1"/></svg>
        Australia</div>
      <div class="volume-box__size">500 ml</div>
    </div>
    <p class="warning warning--blue">Keep out of reach of children</p>
  </section>

  <section class="label label--two">
    <div class="label__kraft"></div>
    <div class="brand"><span>Sea Pines</span><span class="brand__dot"></span></div>
    <svg class="seal" viewBox="0 0 88 88" role="img" aria-label="Recycled bottle badge">
      <circle cx="44" cy="44" r="42" fill="none" stroke="var(--stamp-blue)" stroke-width="2"/>
      <circle cx="44" cy="44" r="26" fill="none" stroke="var(--stamp-blue)" stroke-width="1.5"/>
    </svg>
    <p class="variant variant--bold-dark">Window Cleaner</p>
    <h1 class="product">SHIMMER</h1>
    <p class="tagline">Drop In, Clean Up</p>
    <div class="volume-box">
      <div class="volume-box__origin">Seacliff
        <svg class="volume-box__wave" width="30" height="4" viewBox="0 0 30 4"><path d="M1 3 Q15 0 29 2" fill="none" stroke="var(--slate-blue)" stroke-width="1"/></svg>
        Australia</div>
      <div class="volume-box__size">500 ml</div>
    </div>
    <p class="warning warning--white">Keep out of reach of children</p>
  </section>

  <section class="label label--three">
    <div class="label__kraft"></div>
    <div class="brand"><span>Sea Pines</span><span class="brand__dot"></span></div>
    <svg class="seal" viewBox="0 0 88 88" role="img" aria-label="Recycled bottle badge">
      <circle cx="44" cy="44" r="42" fill="none" stroke="var(--stamp-blue)" stroke-width="2"/>
      <circle cx="44" cy="44" r="26" fill="none" stroke="var(--stamp-blue)" stroke-width="1.5"/>
    </svg>
    <p class="variant variant--bold-blue">Window Cleaner</p>
    <h1 class="product">SHIMMER</h1>
    <p class="tagline">Drop In, Clean Up</p>
    <div class="volume-box">
      <div class="volume-box__origin">Seacliff
        <svg class="volume-box__wave" width="30" height="4" viewBox="0 0 30 4"><path d="M1 3 Q15 0 29 2" fill="none" stroke="var(--slate-blue)" stroke-width="1"/></svg>
        Australia</div>
      <div class="volume-box__size">500 ml</div>
    </div>
    <p class="warning warning--blue">Keep out of reach of children</p>
  </section>

</main>
</body>
</html>
```